Financial Advisor Graphic to Explain Proprietary and Differentiating Investment Strategy

We need a graphic that visualizes how we build a portfolio based on factors of the underlying companies. We use 8 main factors to objectively build an investment porftolio. Our colors are blues, greys (see www.pltvexgroup.com). We are thinking either a venn diagram approach or an atom approach with the factors around the middle "Core Portfolio". This is what differentiates us from everyone in the industry. This will be the key to all of our marketing

Target Market(s)

High net worth investors

Industry/Entity Type

Financial Service

Font styles to use
Serif

Requirements
Must have
• Graphic must be elegant. It is for the financial industry. It should include the following factors (in no order) to build a "Core Portfolio"
• -Counter Cyclical Industries
• -Industry Rate of Recovery
• -Price To Book
• -Absolute Risk
• -Market Capitalization
• -Liquidity
• -Dividend Yield
• -Buy Back Yield
Nice to have
• We are thinking an atom approach or a venn diagram but we are open to new ideas. It must portray the idea that we OBJECTIVELY apply these factors to stock selection to build a core portfolio for our investors. For color pallets see www.pltvexgroup.com It can go beyond the greys and blues but should not be too loud or playful. It can be high tech as long as it portrays seriousness of the financial markets
Should not have
• Can not be playful.

```html
<!DOCTYPE html>
<html lang="en">
<head>
<meta charset="utf-8">
<title>Core Portfolio</title>
<link rel="stylesheet" href="https://fonts.googleapis.com/css2?family=EB+Garamond:ital,wght@1,500&family=PT+Serif&display=swap">
<style>
  :root {
    --bg-royal: #0000ab;
    --title-white: #ffffff;
    --label-ink: #111111;
    --sky: #55b4f5;
    --lavender: #d59bf7;
    --leaf: #99cc55;
    --amber: #f7a03a;
  }
  html, body {
    margin: 0;
    padding: 0;
    overflow: hidden;
    background: var(--bg-royal);
  }
  .canvas {
    position: relative;
    width: 1200px;
    height: 852px;
    background: var(--bg-royal);
    overflow: hidden;
  }
  .title {
    position: absolute;
    top: 118px;
    left: 0;
    width: 100%;
    margin: 0;
    text-align: center;
    font-family: "EB Garamond", "Times New Roman", serif;
    font-style: italic;
    font-weight: 500;
    font-size: 92px;
    line-height: 1;
    color: var(--title-white);
    letter-spacing: 0.5px;
  }
  .factor-diagram {
    position: absolute;
    top: 0;
    left: 0;
  }
  .factor-rings {
    isolation: isolate;
  }
  .factor-ring {
    mix-blend-mode: multiply;
  }
  .ring-sky { fill: var(--sky); }
  .ring-lavender { fill: var(--lavender); }
  .ring-leaf { fill: var(--leaf); }
  .ring-amber { fill: var(--amber); }
  .factor-label {
    font-family: "PT Serif", "Times New Roman", serif;
    font-size: 17px;
    fill: var(--label-ink);
    text-anchor: middle;
  }
</style>
</head>
<body>
<div class="canvas">
  <h1 class="title">Core Portfolio</h1>

  <svg class="factor-diagram" width="1200" height="852" viewBox="0 0 1200 852" aria-label="Eight portfolio factors overlapping around the core portfolio">
    <g class="factor-rings">
      <circle class="factor-ring ring-sky" cx="372" cy="368" r="100"/>
      <circle class="factor-ring ring-lavender" cx="524" cy="368" r="100"/>
      <circle class="factor-ring ring-leaf" cx="674" cy="368" r="100"/>
      <circle class="factor-ring ring-amber" cx="826" cy="368" r="100"/>
      <circle class="factor-ring ring-leaf" cx="448" cy="502" r="100"/>
      <circle class="factor-ring ring-amber" cx="600" cy="502" r="100"/>
      <circle class="factor-ring ring-sky" cx="752" cy="502" r="100"/>
      <circle class="factor-ring ring-lavender" cx="600" cy="636" r="100"/>
    </g>

    <g class="factor-labels">
      <text class="factor-label" x="376" y="350">Counter</text>
      <text class="factor-label" x="376" y="373">Cyclical</text>
      <text class="factor-label" x="376" y="396">Industries</text>

      <text class="factor-label" x="524" y="350">Industry</text>
      <text class="factor-label" x="524" y="373">Rate of</text>
      <text class="factor-label" x="524" y="396">Recovery</text>

      <text class="factor-label" x="674" y="362">Price To</text>
      <text class="factor-label" x="674" y="385">Book</text>

      <text class="factor-label" x="828" y="362">Absolute</text>
      <text class="factor-label" x="828" y="385">Risk</text>

      <text class="factor-label" x="448" y="485">Market</text>
      <text class="factor-label" x="448" y="508">Capitaliza-</text>
      <text class="factor-label" x="448" y="530">tion</text>

      <text class="factor-label" x="600" y="508">Liquidity</text>

      <text class="factor-label" x="752" y="496">Dividend</text>
      <text class="factor-label" x="752" y="519">Yield</text>

      <text class="factor-label" x="600" y="632">Buy Back</text>
      <text class="factor-label" x="600" y="655">Yield</text>
    </g>
  </svg>
</div>
</body>
</html>
```